Anzeigengestaltung für Stelleninserate
Zielgruppe
Wir sind ein in Europa führender Hersteller flexibler Verpackungen, überwiegend für die Branchen Nahrungsmittel, Tiernahrung und Hygiene. Als mittelständisches Familienunternehmen mit Sitz in Feldbrunn entwickeln wir uns sehr dynamisch, haben eine flache Führungshierarchie und setzen auf Eigenverantwortung unserer Mitarbeiter.
Aufgabenstellung
DINA4, Design sollte so gestaltet werden, dass es danach selber in Word bearbeitet werden kann und der Text immer wieder erneuert werden kann, es sollte nur eine Vorlage werden, und auf jegliche Stellenanzeigen anwendbar sein (siehe Anhang), eventuell auch Bilder austauschbar

```html
<!DOCTYPE html>
<html lang="de">
<head>
<meta charset="utf-8">
<title>Stelleninserat – Talvester Verpackungstechnik</title>
<link href="https://fonts.googleapis.com/css2?family=Source+Sans+3:wght@400;600;700&display=swap" rel="stylesheet">
<style>
  :root {
    --brand-blue: #2a5f9e;
    --backdrop: #e6e3e3;
    --paper: #ffffff;
    --ink: #1f1f1f;
    --photo-light: #e9ecee;
    --photo-mid: #cdd3d8;
  }
  * { margin: 0; padding: 0; box-sizing: border-box; }
  html, body {
    width: 848px; height: 1200px; overflow: hidden;
    background: var(--backdrop);
    font-family: "Source Sans 3", "Source Sans Pro", sans-serif;
    color: var(--ink);
  }
  .canvas { position: relative; width: 848px; height: 1200px; }
  .page {
    position: absolute; left: 37px; top: 52px; width: 774px; height: 1095px;
    background: var(--paper);
  }
  .frame {
    position: absolute; left: 52px; top: 66px; width: 744px; height: 1068px;
    border: 4px solid var(--brand-blue);
  }
  .hero-photo {
    position: absolute; left: 69px; top: 85px; width: 709px; height: 337px;
    background: linear-gradient(160deg, #f4f5f6 0%, var(--photo-light) 45%, var(--photo-mid) 70%, #eef0f1 100%);
  }
  .brand-plate {
    position: absolute; left: 468px; top: 121px; width: 289px; height: 69px;
    background: var(--paper);
    display: flex; align-items: center; justify-content: center;
  }
  .brand-name {
    font-weight: 700; font-size: 36px; letter-spacing: 1px;
    color: var(--brand-blue); text-transform: uppercase;
  }
  .headline-bar {
    position: absolute; left: 69px; top: 404px; width: 418px; height: 46px;
    background: var(--brand-blue);
  }
  .headline {
    position: absolute; left: 30px; top: 3px;
    color: #fff; font-weight: 700; font-size: 32px; line-height: 40px;
  }
  .intro {
    position: absolute; left: 99px; top: 462px; width: 640px;
    font-size: 12.6px; line-height: 17.8px;
  }
  .invite {
    position: absolute; left: 99px; top: 533px;
    font-size: 12.4px; font-weight: 600;
  }
  .job-title {
    position: absolute; left: 99px; top: 553px;
    font-size: 19.5px; font-weight: 700; color: var(--brand-blue);
  }
  .section { position: absolute; left: 99px; width: 420px; }
  .section h3 { font-size: 12.4px; font-weight: 600; line-height: 18px; margin-bottom: 5px; }
  .section ul { list-style: none; padding-left: 16px; }
  .section li { font-size: 12.6px; line-height: 17.9px; }
  .section.tasks { top: 586px; width: 620px; }
  .section.profile { top: 783px; }
  .section.offer { top: 893px; }
  .contact-box { position: absolute; left: 526px; top: 756px; width: 221px; height: 225px; }
  .contact-box svg { position: absolute; inset: 0; }
  .contact-text {
    position: absolute; left: 0; top: 16px; width: 221px; text-align: center;
    font-size: 12.6px; line-height: 17.9px;
  }
  .contact-text .company { font-weight: 600; color: var(--brand-blue); }
  .contact-text .gap { height: 17.9px; }
  .footer-band {
    position: absolute; left: 69px; top: 1032px; width: 709px; height: 82px;
    background: var(--brand-blue);
  }
  .footer-text {
    position: absolute; left: 30px; top: 12px; width: 420px;
    color: #fff; font-size: 12.6px; line-height: 18px;
  }
  .footer-text strong { font-weight: 700; }
  .building-mat {
    position: absolute; left: 555px; top: 902px; width: 163px; height: 182px;
    background: var(--paper);
  }
  .building-photo {
    position: absolute; left: 7px; top: 6px; width: 150px; height: 164px;
    background: linear-gradient(180deg, #4f86b8 0%, #7aa6cb 40%, #4b5158 55%, #6e7378 80%, #b8bcbf 100%);
  }
</style>
</head>
<body>
<div class="canvas">
  <div class="page"></div>
  <div class="frame"></div>

  <div class="hero-photo" role="img" aria-label="Foto einer hellen Produktionshalle mit Druckmaschine und Folienrollen"></div>
  <div class="brand-plate"><span class="brand-name">Talvester</span></div>

  <div class="headline-bar"><h1 class="headline">Wir suchen Verstärkung</h1></div>

  <p class="intro">Wir sind ein in Europa führender Hersteller flexibler Verpackungen, überwiegend für die Branchen Nahrungsmittel, Tiernahrung und Hygiene. Als mittelständisches Familienunternehmen mit Sitz in Feldbrunn entwickeln wir uns sehr dynamisch, haben eine flache Führungshierarchie und setzen auf Eigenverantwortung unserer Mitarbeiter.</p>

  <p class="invite">Kommen Sie in unser Team als</p>
  <h2 class="job-title">Mitarbeiter für Labor und Qualitätssicherung (m/w/d).</h2>

  <section class="section tasks">
    <h3>Ihre Verantwortung bei uns:</h3>
    <ul>
      <li>Durchführung von Qualitätsprüfungen für die Freigabe zur Auslieferung unserer Produkte</li>
      <li>Erstellung von QM-konformer bzw. nachvollziehbarer Dokumentation</li>
      <li>Überprüfung der Einhaltung von Hygiene-, Qualitäts- und Sicherheitsrichtlinien</li>
      <li>Erkennung und Meldung von Abweichungen der Vorgaben bzw. Qualitätsmängeln</li>
      <li>Sicherstellung der permanenten Betriebsbereitschaft unserer Prüfgeräte</li>
      <li>Bearbeitung von internen und externen Reklamationen</li>
      <li>Unterstützung bei der Durchführung von Projektarbeiten</li>
      <li>Erarbeitung von Verbesserungsvorschlägen</li>
      <li>Erstellen von Protokollen und Prüfberichten</li>
    </ul>
  </section>

  <section class="section profile">
    <h3>Ihre Verantwortung bei uns:</h3>
    <ul>
      <li>Abgeschlossene technische Ausbildung</li>
      <li>Selbstbewusstes Auftreten und Durchsetzungsvermögen</li>
      <li>Selbstständige und zielorientierte Arbeitsweise</li>
      <li>Teamfähige Persönlichkeit</li>
    </ul>
  </section>

  <section class="section offer">
    <h3>Ihre Verantwortung bei uns:</h3>
    <ul>
      <li>Eigenverantwortliches Aufgabengebiet in einem dynamischen<br>Umfeld und motivierten Team</li>
      <li>Mitarbeit in einem erfolgreich geführten Familienunternehmen</li>
      <li>Angenehmes Arbeitsumfeld</li>
      <li>Persönliche und fachliche Entwicklungsmöglichkeiten</li>
    </ul>
  </section>

  <aside class="contact-box">
    <svg width="221" height="225" viewBox="0 0 221 225" aria-hidden="true">
      <path d="M29 223 H2 V2 H219 V223 H192" fill="none" stroke="var(--brand-blue)" stroke-width="3"/>
    </svg>
    <div class="contact-text">
      <div class="company">Talvester Verpackungstechnik GmbH</div>
      <div>Lindenfeldweg 4 B - 6840&nbsp; Feldbrunn</div>
      <div class="gap"></div>
      <div>+43 5500 10400</div>
      <div>+43 5500 10400 - 12</div>
      <div>karriere@talvester.example</div>
      <div>www.talvester.example</div>
    </div>
  </aside>

  <div class="footer-band">
    <p class="footer-text">Wir freuen uns über Ihre Bewerbung, welche Sie bitte direkt an <strong>karriere@talvester.example</strong> senden, am liebsten heute noch, damit wir Sie möglichst rasch persönlich kennenlernen können.</p>
  </div>

  <div class="building-mat">
    <div class="building-photo" role="img" aria-label="Foto des dunklen, modernen Firmengebäudes unter blauem Himmel"></div>
  </div>
</div>
</body>
</html>
```